Ductless Mini Split Business Website

Amber Kite Services is looking to design an eye catching educational website about installing Ductless mini splits.

Similar to this company.
https://www.cedarcoolair.com/

```html
<!DOCTYPE html>
<html lang="en">
<head>
<meta charset="utf-8">
<title>Amber Kite Services – Ductless Experts</title>
<link href="https://fonts.googleapis.com/css2?family=Lato:wght@400;700;900&display=swap" rel="stylesheet">
<style>
:root{
  --yellow:#f8d40c;
  --yellow-deep:#d4b40a;
  --ink:#222;
  --band:#333436;
  --panel:#3c3d3f;
  --light:#e9ecef;
  --footer:#151515;
  --white:#fff;
}
*{box-sizing:border-box;margin:0;padding:0}
html,body{width:1200px;height:2788px;overflow:hidden}
body{position:relative;font-family:'Lato',sans-serif;color:var(--ink);background:var(--light)}
.abs{position:absolute}
.center{text-align:center}

.site-header{left:0;top:0;width:1200px;height:95px;background:#f0f0f0}
.brand{left:140px;top:24px;width:180px;text-align:center}
.brand-name{display:flex;align-items:center;justify-content:center;gap:6px;font-weight:900;font-size:17px;color:var(--ink);white-space:nowrap}
.brand-name i{width:12px;height:12px;background:var(--yellow);display:inline-block;border-radius:50%;flex:none}
.brand-tag{font-weight:700;font-size:14px;color:var(--ink);margin-top:18px;letter-spacing:.3px}
.nav{left:350px;top:0;height:95px;display:flex;align-items:center;font-size:14px;font-weight:700}
.nav a{color:var(--ink);text-decoration:none;padding:0 9px;height:95px;line-height:100px}
.nav a.active{background:var(--band);color:var(--yellow)}

.hero{left:0;top:95px;width:1200px;height:528px;background:linear-gradient(135deg,#5a5550,#3a3633 45%,#6b645c);}
.hero-title{left:0;top:188px;width:1200px;font-size:63px;font-weight:900;color:var(--yellow)}
.hero-sub{left:0;top:255px;width:1200px;font-size:23px;font-weight:700;color:var(--white)}
.divider{display:flex;align-items:center;justify-content:center;gap:10px}
.divider span{height:2px;background:var(--white);width:136px}
.divider b{width:8px;height:8px;border-radius:50%;background:var(--yellow)}
.btn{background:var(--yellow);color:var(--ink);font-weight:700;border-radius:4px;outline:2px dashed var(--yellow);outline-offset:4px;text-align:center}
.hero-btn{left:499px;top:336px;width:222px;height:48px;line-height:48px;font-size:16px}

.band{left:0;width:1200px;height:50px;background:var(--band)}
.band h2{position:absolute;top:9px;font-size:21px;font-weight:900;color:var(--yellow);text-align:center}
.band .divider{position:absolute;top:36px}
.band .divider span{width:168px}

.intro{left:0;top:673px;width:1200px;height:474px;background:linear-gradient(180deg,#eef1f3,#d9dde1 60%,#eceff1)}
.intro-card{left:122px;top:8px;width:405px;height:458px;background:var(--panel);padding:0 30px}
.intro-card .divider span{width:165px}
.intro-card h3{color:var(--yellow);font-size:19px;font-weight:700;margin-top:18px;line-height:22px}
.intro-card p{color:var(--white);font-size:18.5px;line-height:22px;margin-top:20px}
.video{left:642px;top:94px;width:406px;height:274px;border:2px solid #222;padding:3px;background:#222}
.video-inner{width:100%;height:100%;border:2px solid #ccc;background:linear-gradient(135deg,#3e3f42,#25272a);display:flex;align-items:center;justify-content:center}

.services{left:0;top:1199px;width:1200px;height:555px;background:linear-gradient(180deg,#eef1f3,#dfe3e6 60%,#eef1f3)}
.tile{width:179px;height:159px;border-radius:5px;overflow:hidden;position:absolute}
.tile .photo{height:122px}
.tile .label{height:37px;background:rgba(40,40,40,.9);color:var(--yellow);font-size:8.5px;font-weight:700;text-align:center;line-height:37px;text-transform:uppercase}
.more-btn{left:486px;top:467px;width:231px;height:48px;line-height:48px;font-size:16px;font-weight:900;outline:none}

.contact{left:0;top:1754px;width:1200px;height:678px;background:linear-gradient(180deg,#2d2d2c,#3f3d38 50%,#262625)}
.contact h2{left:0;top:42px;width:727px;font-size:31px;font-weight:900;color:var(--yellow)}
.contact .lead{left:0;top:100px;width:727px;font-size:16px;font-weight:700;color:var(--white);line-height:25px}
.contact .lead em{font-style:normal;color:var(--yellow)}
.field{background:rgba(200,200,200,.55);color:var(--white);font-size:14px;padding:9px 8px;height:33px;border-radius:2px}
.send-btn{left:279px;top:613px;width:169px;height:37px;line-height:37px;font-size:12px}
.why{left:644px;top:24px;width:405px;height:550px;background:rgba(213,183,10,.9);color:var(--white)}
.why h2{left:58px;top:20px;width:320px;font-size:31px;font-weight:700;line-height:37px}
.why-item{left:16px;display:flex;gap:12px;width:370px}
.why-item svg{flex:none}
.why-item h4{font-size:14px;font-weight:900}
.why-item p{font-size:11.5px;line-height:15px}

.footer{left:0;top:2432px;width:1200px;height:356px;background:var(--footer);color:var(--white)}
.footer h4{color:var(--yellow);font-size:16px;font-weight:700;white-space:nowrap}
.footer p{font-size:14.5px;line-height:27px}
.footer .yl{color:var(--yellow)}
.social{display:flex;gap:32px}
.social i{width:31px;height:31px;border-radius:50%;background:var(--yellow);display:block}
</style>
</head>
<body>

<header class="site-header abs">
  <div class="brand abs">
    <div class="brand-name"><i></i>Amber Kite Services</div>
    <div class="brand-tag">DUCTLESS EXPERTS</div>
  </div>
  <nav class="nav abs">
    <a class="active">Home</a><a>About Us</a><a>Ductless Heat Pump</a><a>Ductless Heat Pump FAQ</a><a>Financing</a><a>Reviews</a><a>Contact Us</a>
  </nav>
</header>

<section class="hero abs" role="img" aria-label="Man working on a laptop in a bright modern office">
  <h1 class="hero-title abs center">DUCTLESS DOES IT BETTER</h1>
  <div class="hero-sub abs center">LET OREGON DUCTLESS CREW SHOW YOU HOW</div>
  <div class="divider abs" style="left:0;top:301px;width:1200px"><span></span><b></b><span></span></div>
  <div class="btn hero-btn abs">GET IN TOUCH WITH US</div>
</section>

<div class="band abs" style="top:623px">
  <h2 style="left:150px;width:393px">DUCTLESS DOES IT BETTER</h2>
  <div class="divider" style="left:150px;width:393px"><span></span><b></b><span></span></div>
  <h2 style="left:650px;width:392px">OREGON DUCTLESS TIMELAPSE</h2>
  <div class="divider" style="left:650px;width:392px"><span></span><b></b><span></span></div>
</div>

<section class="intro abs">
  <div class="intro-card abs">
    <div class="divider" style="margin-top:6px"><span></span><b></b><span></span></div>
    <h3>HELPING PORTLAND &amp; SURROUNDING AREAS GO DUCTLESS</h3>
    <p>Experience maximum comfort, better indoor air quality, and lower utility bills by installing ductless heat pumps in your home. As the premier company for everything ductless related, Cedar Cool Air Crew offers a wide selection of quality ductless systems from industry-leading manufacturers such as Northwind and Aerlo. We are also the experts when it comes to unparalleled ductless solutions. Whether you need repairs or maintenance for an existing unit or are considering switching your baseboard heating with a ductless heat pump, our trained technicians can do it all.</p>
    <div class="divider" style="margin-top:14px"><span></span><b></b><span></span></div>
  </div>
  <div class="video abs">
    <div class="video-inner" role="img" aria-label="Video still of the service team standing in an office">
      <svg width="40" height="46" viewBox="0 0 40 46"><path d="M2 2 L38 23 L2 44 Z" fill="#fff"/></svg>
    </div>
  </div>
</section>

<div class="band abs" style="top:1149px">
  <h2 style="left:400px;width:400px">OREGON DUCTLESS TIMELAPSE</h2>
  <div class="divider" style="left:400px;width:400px"><span></span><b></b><span></span></div>
</div>

<section class="services abs">
  <div class="tile" style="left:157px;top:58px"><div class="photo" role="img" aria-label="Baseboard heater under a window" style="background:linear-gradient(#8b93a3,#d7dade 40%,#9a6a3e)"></div><div class="label">Baseboard Heat Replacement</div></div>
  <div class="tile" style="left:393px;top:58px"><div class="photo" role="img" aria-label="Living room with sofa" style="background:linear-gradient(#e8e4dc,#8a7a68)"></div><div class="label">Ductless for Addition &amp; Remodels</div></div>
  <div class="tile" style="left:626px;top:58px"><div class="photo" role="img" aria-label="Metal vent parts" style="background:linear-gradient(135deg,#f0f0f0,#9a9a9a)"></div><div class="label">Ductless Heat Pump FAQ</div></div>
  <div class="tile" style="left:862px;top:58px"><div class="photo" role="img" aria-label="Technician installing an indoor unit" style="background:linear-gradient(135deg,#6a6f78,#dfe3e8)"></div><div class="label">Ductless Installation</div></div>
  <div class="tile" style="left:157px;top:271px"><div class="photo" role="img" aria-label="Technician servicing a wall unit" style="background:linear-gradient(135deg,#c9d8ec,#6d7a8c)"></div><div class="label">Ductless Maintenance</div></div>
  <div class="tile" style="left:393px;top:271px"><div class="photo" role="img" aria-label="Technician repairing an open unit" style="background:linear-gradient(135deg,#e2e2e2,#555)"></div><div class="label">Ductless Repairs</div></div>
  <div class="tile" style="left:626px;top:271px"><div class="photo" role="img" aria-label="Wall unit with remote" style="background:linear-gradient(#f4f4f4,#c8c8c8)"></div><div class="label">Ductless Warranty</div></div>
  <div class="tile" style="left:862px;top:271px"><div class="photo" role="img" aria-label="Bright kitchen interior" style="background:linear-gradient(#ddd6cc,#8e7c6b)"></div><div class="label">Whole House Ductless</div></div>
  <div class="btn more-btn abs">MORE DUCTLESS SERVICE</div>
</section>

<section class="contact abs" role="img" aria-label="House exterior at dusk">
  <h2 class="abs center">CONTACT US TODAY</h2>
  <div class="lead abs center">FILL OUT THE FORM BELOW<br>OR CALL CEDAR COOL AIR CREW AT<br><em>(503) 555-0142</em></div>
  <div class="divider abs" style="left:177px;width:374px;top:190px"><span style="width:170px"></span><b></b><span style="width:170px"></span></div>
  <div class="field abs" style="left:153px;top:239px;width:183px">First Name</div>
  <div class="field abs" style="left:375px;top:239px;width:183px">Last Name</div>
  <div class="field abs" style="left:153px;top:308px;width:183px">Phone</div>
  <div class="field abs" style="left:375px;top:308px;width:183px">Email</div>
  <div class="field abs" style="left:153px;top:379px;width:405px">Are you a new customer ?</div>
  <div class="field abs" style="left:153px;top:449px;width:405px;height:125px">Message</div>
  <div class="btn send-btn abs">SEND INFORMATION</div>

  <div class="why abs">
    <div class="divider abs" style="left:16px;top:8px;width:373px"><span style="width:165px"></span><b></b><span style="width:165px"></span></div>
    <h2 class="abs">Why Choose Cedar<br>Cool Air Crew?</h2>
    <div class="divider abs" style="left:16px;top:130px;justify-content:flex-start;gap:14px"><b></b><span style="width:168px"></span></div>
    <div class="why-item abs" style="top:180px">
      <svg width="40" height="36" viewBox="0 0 40 36" fill="none" stroke="#fff" stroke-width="2"><rect x="6" y="3" width="26" height="30" rx="2"/><path d="M12 11h14M12 17h14M12 23h10"/></svg>
      <div><h4>0% FINANCING FOR 60 MONTHS</h4><p>Providing options to our customers where it matters most. Offer applies to Corvel systems.</p></div>
    </div>
    <div class="why-item abs" style="top:280px">
      <svg width="38" height="40" viewBox="0 0 38 40" fill="none" stroke="#fff" stroke-width="2"><path d="M3 16a16 12 0 0 1 32 0z"/><path d="M19 16v8"/><circle cx="19" cy="31" r="7"/></svg>
      <div><h4>365 DAY, MONEY BACK GUARANTEE</h4><p>We have integrity, and stand behind our services to ensure that you are satisfied.</p></div>
    </div>
    <div class="why-item abs" style="top:372px">
      <svg width="36" height="40" viewBox="0 0 36 40" fill="none" stroke="#fff" stroke-width="2"><path d="M18 3l13 5v11c0 9-6 15-13 18C11 34 5 28 5 19V8z"/><path d="M11 20l5 5 9-10"/></svg>
      <div><h4>WE ARE THE EXPERTS IN DUCTLESS SERVICES</h4><p>Not only can we perform the services with precision, but we can also educate you on why ductless is the way to do.</p></div>
    </div>
    <div class="divider abs" style="left:16px;top:528px;width:373px"><span style="width:165px"></span><b></b><span style="width:165px"></span></div>
  </div>
</section>

<footer class="footer abs">
  <div class="abs center" style="left:140px;top:40px;width:190px">
    <div class="brand-name" style="color:var(--yellow);font-size:16px"><i></i>Amber Kite Services</div>
    <div style="color:var(--yellow);font-weight:700;font-size:16px;margin-top:18px">DUCTLESS EXPERTS</div>
  </div>
  <h4 class="abs center" style="left:150px;top:144px;width:163px">CONTACT US</h4>
  <div class="abs center" style="left:140px;top:172px;width:183px;font-size:25px;font-weight:700">503-555-0142</div>
  <h4 class="abs center" style="left:150px;top:274px;width:168px">FOLLOW US</h4>
  <div class="social abs" style="left:156px;top:310px"><i></i><i></i><i></i></div>

  <div class="abs" style="left:381px;top:70px">
    <h4>Oregon Ductless Location</h4>
    <p>2280 SE Alder Park Rd,<br>Suite B12<br>Milwaukie, OR 97222<br><span class="yl">Map &amp; Directions [+]</span></p>
  </div>
  <div class="abs" style="left:627px;top:70px">
    <h4>A Division of Ridge Heating</h4>
    <p>7410 SW Birchwood Ave.<br>Tualatin, OR 97062<br><span class="yl" style="font-size:16px">Map &amp; Directions [+]</span></p>
  </div>
  <div class="abs" style="left:877px;top:64px">
    <h4 style="font-size:19px;font-weight:400">Quick Links</h4>
    <p>Home<br>About Us<br>Ductless Heat Pumps<br>Ductless Heat Pumps FAQ<br>Financing<br>Contact Us<br>Privacy Policy<br>Site Map</p>
  </div>
  <div class="abs center" style="left:0;top:318px;width:1200px;font-size:16px">© 2019 All Rights Reserved.</div>
</footer>

</body>
</html>
```